Packaging Label Design for Hair Styling Product

Our company is launching a new hair styling product in early June. Need a designer to help on the packaging label for the hair product.
For more details please go to our website velmorick.co

Target Market(s)

Male Age 13-34. Men who likes hair pomade/hair clay and other hair products

Industry/Entity Type

Hair And Beauty

Font styles to use
Sans Serif
Script

Requirements
Must have
• 1. Company logo must be used on circular and rectangular designs.
2.Company name must be used on rectangular design only.
3.Silver polyester label material will be used.
4.Colour theme shall be in colours such as “Black”, “Dark Grey” and “Silver”.
5.A black orchid artwork must be featured in the design.
6.The following copywriting must be included in the design,
7.“Quarry Fiber Paste” on both circular and rectangular designs.
8. Talbrook & Co. Logo

Circular Design Label
-Singapore’s Homebrew
-100mL
-Strong Hold| Charcoal Infused

Rectangular Design Label
-Ingredients: WATER (AQUA), EUPHORBIA CERIFERA (CANDELILLA) WAX, KAOLIN, PEG-40 HYDROGENATED CASTOR OIL, PRUNUS ARMENIACA (APRICOT) KERNEL OIL, CETEARYL ALCOHOL, CETEARYL GLUCOSIDE, RICINUS COMMUNIS (CASTOR) OIL, BENTONITE, FRAGRANCE, PHENOXYETHANOL, CAPRYLYL GLYCOL, SORBIC ACID, ACTIVATED CHARCOAL.
-Required to include a “12m” logo. *Refer to example design.
-“For best result, work a dime-sized amount between your palms and apply on blow-dried hair. Comb or shape your hair to desired style. Restyle anytime. Use more if needed.”
-High Texture| Matte Finish| Easy Wash-out| Easy Application| Featherweight
-Made in Singapore
-Talbrook & Co. Pte. Ltd.
-742 Bedok Tirah Avenue 5 #06-2817
Singapore 480762 | www.velmorick.co
Nice to have
• Reference from the previous hair clay design. Please refer to attached document.
Should not have
• Please refer to attachment on the colors.

```html
<!DOCTYPE html>
<html lang="en">
<head>
<meta charset="utf-8">
<title>Quarry Fiber Paste — Label Set</title>
<link rel="stylesheet" href="https://fonts.googleapis.com/css2?family=Kaushan+Script&family=Cormorant+Garamond:wght@500&family=Open+Sans:wght@300;700&family=Roboto+Condensed:wght@400;700&display=swap">
<style>
  :root {
    --label-grey: #949493;
    --page: #ffffff;
    --ink-white: #ffffff;
    --brand-cream: #efdcae;
    --orchid-navy: #25308f;
  }
  * { box-sizing: border-box; margin: 0; padding: 0; }
  html, body { width: 1200px; height: 1200px; overflow: hidden; background: var(--page); }
  .canvas { position: relative; width: 1200px; height: 1200px; }

  /* Circular lid label */
  .lid-label { position: absolute; left: 430px; top: 230px; width: 340px; height: 340px; }
  .lid-label svg { display: block; }
  .lid-brand {
    font-family: "Cormorant Garamond", serif; font-weight: 500;
    font-size: 14px; letter-spacing: 2px; fill: var(--brand-cream);
  }
  .lid-title { font-family: "Kaushan Script", cursive; font-size: 38px; fill: var(--ink-white); }
  .lid-tagline {
    font-family: "Open Sans", sans-serif; font-weight: 300;
    font-size: 16px; letter-spacing: 2.4px; fill: var(--ink-white);
  }
  .lid-volume, .lid-arc-text {
    font-family: "Open Sans", sans-serif; font-weight: 700;
    font-size: 13px; fill: var(--ink-white);
  }

  /* Rectangular wrap label */
  .wrap-label {
    position: absolute; left: 16px; top: 650px; width: 1168px; height: 124px;
    background: var(--label-grey); overflow: hidden; color: var(--ink-white);
    font-family: "Roboto Condensed", sans-serif;
  }
  .wrap-orchid { position: absolute; left: 496px; top: 0; width: 232px; height: 124px; }
  .wrap-company { position: absolute; left: 27px; top: 22px; }
  .wrap-brand {
    display: flex; align-items: center; gap: 6px;
    font-family: "Cormorant Garamond", serif; font-weight: 500;
    font-size: 12px; letter-spacing: 1.5px; color: var(--brand-cream); margin-bottom: 14px;
  }
  .wrap-brand .dot { width: 8px; height: 8px; border-radius: 50%; background: var(--brand-cream); }
  .wrap-company .legal {
    font-family: "Cormorant Garamond", serif; font-weight: 500; font-size: 13px; line-height: 15px;
  }
  .wrap-company .address { font-size: 11px; line-height: 14px; }
  .wrap-ingredients {
    position: absolute; left: 258px; top: 14px; width: 179px;
    font-size: 8px; line-height: 11.4px; text-align: justify;
  }
  .wrap-ingredients strong { font-weight: 700; }
  .wrap-front { position: absolute; left: 480px; top: 22px; width: 320px; }
  .wrap-front .brand {
    font-family: "Cormorant Garamond", serif; font-weight: 500; font-size: 14px;
    letter-spacing: 2px; color: var(--brand-cream); padding-left: 92px;
  }
  .wrap-front .title { font-family: "Kaushan Script", cursive; font-size: 33px; line-height: 44px; padding-left: 22px; }
  .wrap-usage { position: absolute; right: 27px; top: 14px; width: 320px; text-align: right; }
  .wrap-usage .claims { font-weight: 700; font-size: 12.5px; line-height: 16px; }
  .wrap-usage .directions { font-size: 8.3px; line-height: 11.4px; margin-top: 6px; }
  .wrap-usage .origin { font-weight: 700; font-size: 11px; margin-top: 10px; padding-right: 3px; }
</style>
</head>
<body>
<main class="canvas">

  <section class="lid-label" aria-label="Circular lid label">
    <svg width="340" height="340" viewBox="0 0 340 340">
      <defs>
        <clipPath id="lid-clip"><circle cx="170" cy="170" r="170"/></clipPath>
        <radialGradient id="orchid-tone" cx="50%" cy="50%" r="50%">
          <stop offset="0%" stop-color="#25308f" stop-opacity="0.32"/>
          <stop offset="100%" stop-color="#25308f" stop-opacity="0"/>
        </radialGradient>
        <path id="lid-arc" d="M 32 170 A 138 138 0 0 0 308 170"/>
      </defs>
      <circle class="lid-base" cx="170" cy="170" r="170" fill="#949493"/>
      <g clip-path="url(#lid-clip)">
        <ellipse role="img" aria-label="Black orchid line artwork" cx="198" cy="160" rx="95" ry="175"
                 transform="rotate(25 198 160)" fill="url(#orchid-tone)"/>
      </g>
      <circle cx="130" cy="48" r="4" fill="#efdcae"/>
      <text class="lid-brand" x="140" y="53">TALBROOK &amp; CO.</text>
      <text class="lid-title" x="170" y="178" text-anchor="middle">Quarry Fiber Paste</text>
      <text class="lid-tagline" x="170" y="200" text-anchor="middle">SINGAPORE’S HOMEBREW</text>
      <text class="lid-volume" x="170" y="277" text-anchor="middle">100mL</text>
      <text class="lid-arc-text"><textPath href="#lid-arc" startOffset="50%" text-anchor="middle">Strong Hold | Charcoal Infused</textPath></text>
    </svg>
  </section>

  <section class="wrap-label" aria-label="Rectangular wrap label">
    <svg class="wrap-orchid" viewBox="0 0 232 124" role="img" aria-label="Black orchid line artwork">
      <defs>
        <radialGradient id="wrap-orchid-tone" cx="50%" cy="50%" r="50%">
          <stop offset="0%" stop-color="#25308f" stop-opacity="0.3"/>
          <stop offset="100%" stop-color="#25308f" stop-opacity="0"/>
        </radialGradient>
      </defs>
      <ellipse cx="130" cy="62" rx="120" ry="80" fill="url(#wrap-orchid-tone)"/>
    </svg>

    <div class="wrap-company">
      <div class="wrap-brand"><span class="dot"></span>TALBROOK &amp; CO.</div>
      <p class="legal">Talbrook &amp; Co. Pte. Ltd.</p>
      <p class="address">742 Bedok Tirah Avenue 5 #06-2817<br>Singapore 480762 | www.velmorick.co</p>
    </div>

    <p class="wrap-ingredients"><strong>INGREDIENTS:</strong> WATER (AQUA), EUPHORBIA CERIFERA (CANDELILLA) WAX, KAOLIN, PEG-40 HYDROGENATED CASTOR OIL, PRUNUS ARMENIACA (APRICOT) KERNEL OIL, CETEARYL ALCOHOL, CETEARYL GLUCOSIDE, RICINUS COMMUNIS (CASTOR) OIL, BENTONITE, FRAGRANCE, PHENOXYETHANOL, CAPRYLYL GLYCOL, SORBIC ACID, ACTIVATED CHARCOAL.</p>

    <div class="wrap-front">
      <p class="brand">Talbrook &amp; Co.</p>
      <p class="title">Quarry Fiber Paste</p>
    </div>

    <div class="wrap-usage">
      <p class="claims">High Texture | Matte Finish | Easy Wash-out<br>Easy Application | Featherweight</p>
      <p class="directions">For best result, work a dime-sized amount between your palms and apply on blow-dried hair. Comb or shape your hair to desired style. Restyle anytime. Use more if needed.</p>
      <p class="origin">Made in Singapore</p>
    </div>
  </section>

</main>
</body>
</html>
```